Breezeway Climate Business Card Design

Design new, 2 sides, business cards for a residential and light commercial heating, air conditioning contractor.

Target Market(s)

Homeowners, small businesses

Industry/Entity Type

Business

Contact Information for Business Card

Dominic Vasquerelli
Phone - 555-214-6837
Email
Address - PO box 618
Millbrook NJ 07999
Website - www.BreezewayClimateLLC.example

Requirements
Must have
• logo, company colors, standard size with no die cut, so I can use printhaven

```html
<!DOCTYPE html>
<html lang="en">
<head>
<meta charset="utf-8">
<title>Breezeway Climate Business Cards</title>
<link href="https://fonts.googleapis.com/css2?family=Open+Sans:wght@400;600;700&display=swap" rel="stylesheet">
<style>
  :root {
    --backdrop: #a3a2a3;
    --card: #ffffff;
    --brand-red: #9a1f33;
    --brand-orange: #f0931e;
    --ink: #2b2b2b;
    --muted: #6b6b6b;
    --rule: #333333;
  }
  * { box-sizing: border-box; margin: 0; padding: 0; }
  html, body { width: 1200px; height: 1200px; overflow: hidden; }
  body {
    background: var(--backdrop);
    font-family: "Open Sans", Arial, sans-serif;
    position: relative;
  }
  .card {
    position: absolute;
    left: 220px;
    width: 760px;
    height: 434px;
    background: var(--card);
    box-shadow: 0 6px 18px rgba(0,0,0,0.25);
  }
  .card--front { top: 120px; }
  .card--back { top: 646px; }

  .brand {
    position: absolute;
    display: flex;
    align-items: center;
    gap: 14px;
  }
  .brand__dot {
    width: 34px; height: 34px;
    border-radius: 50%;
    background: var(--brand-orange);
    flex: none;
  }
  .brand__name {
    font-weight: 700;
    color: var(--brand-red);
    font-size: 40px;
    letter-spacing: 0.5px;
    white-space: nowrap;
  }
  .card--front .brand { left: 50%; top: 50%; transform: translate(-50%, -50%); }
  .card--back .brand { left: 44px; top: 50%; transform: translateY(-50%); }
  .card--back .brand__name { font-size: 31px; }
  .card--back .brand__dot { width: 28px; height: 28px; }

  .divider {
    position: absolute;
    left: 410px;
    top: 120px;
    width: 1.5px;
    height: 200px;
    background: var(--rule);
  }
  .contact {
    position: absolute;
    left: 440px;
    top: 112px;
    color: var(--ink);
    font-size: 15px;
    line-height: 1.3;
  }
  .contact__name { color: var(--brand-orange); font-weight: 600; font-size: 20px; }
  .contact__title { color: var(--muted); font-size: 15px; margin-bottom: 18px; }
  .contact__address { margin-bottom: 18px; }
  .contact__row { display: flex; align-items: center; gap: 10px; }
  .contact__row svg { width: 13px; height: 13px; flex: none; }
</style>
</head>
<body>
  <section class="card card--front">
    <div class="brand">
      <span class="brand__dot"></span>
      <span class="brand__name">Breezeway Climate</span>
    </div>
  </section>

  <section class="card card--back">
    <div class="brand">
      <span class="brand__dot"></span>
      <span class="brand__name">Breezeway Climate</span>
    </div>
    <div class="divider"></div>
    <div class="contact">
      <div class="contact__name">Dominic Vasquerelli</div>
      <div class="contact__title">President</div>
      <div class="contact__address">PO box 618<br>Millbrook NJ 07999</div>
      <div class="contact__row">
        <svg viewBox="0 0 16 16"><path fill="#c0392b" d="M3 1l3 3-1.5 2c1 2 3 4 5 5l2-1.5 3 3-2 2C7 14 2 9 1 3z"/></svg>
        <span>555-214-6837</span>
      </div>
      <div class="contact__row">
        <svg viewBox="0 0 16 16"><rect x="1" y="3" width="14" height="10" fill="#c0392b"/><path d="M1 3l7 6 7-6" stroke="#fff" stroke-width="1.4" fill="none"/></svg>
        <span>info@breezewayclimate.example</span>
      </div>
      <div class="contact__row">
        <svg viewBox="0 0 16 16"><circle cx="8" cy="8" r="6.5" fill="none" stroke="#c0392b" stroke-width="1.4"/><path d="M1.5 8h13M8 1.5c-3 3.5-3 9.5 0 13M8 1.5c3 3.5 3 9.5 0 13" stroke="#c0392b" stroke-width="1.1" fill="none"/></svg>
        <span>www.BreezewayClimateLLC.example</span>
      </div>
    </div>
  </section>
</body>
</html>
```